Business card design needed

I need a business card for a new company based in Perth, Western Australia, called KT Power Pty Ltd.

I'm the sole proprietor, and have 25 years' experience in directorship, senior commercial/business development/strategy roles in the oil & gas industry with both supermajors and junior listed companies. I also have interests in renewable energy (and am co-founder and director of a separate renewable energy start-up company). KT Power will be the vehicle for me to contract my services, principally in the oil & gas industry (although this will include directorship services to the renewable energy company). These services will include general consultancy in my areas of expertise, and contracting to provide senior management/director services to start-up or junior oil and gas companies.

I'm looking for a design that communicates professionalism, dynamism, experience, strategic skills and growth.

My ConnectHub profile may also be useful context;

"I have a real passion for discovering new investment opportunities and turning them from talk into reality. Right now my focus is on oil, gas and energy ventures. I’m always on the look out for compelling new investment opportunities where I can bring my leadership and strategic insight to bear to make a real difference by delivering transformational results.

I spent 24 years with HX where I built up extensive international experience in oil, gas and energy and was a member of the company’s “fast track” development programme. As an entrepreneurial senior commercial leader, strategic thinker and tactical dealmaker I was responsible for numerous deals such as divestments, farm-ins, asset swaps, new acreage bids, unitizations, gas and LNG sales, creating billions of dollars of value for HX. These deals frequently broke new ground and/or required an innovative approach that delivered results in excess of what the business thought achievable. I have held senior executive and director roles covering Exploration & Production, Mergers & Acquisitions, Business Development, LNG Marketing, Joint Venture Management, Gas & Power and Corporate head office. International assignments included UK, Australia, Indonesia, Norway & Belgium.

I’m a member of the Guild of Global Fuel Brokers (GGFB) and the Southern Council of Board Members (SCBM).

Board experience comprises four directorships and two alternate directorships of Australian companies, and directorship of a Not for Profit organisation.

Specialties
Strategy, Business Development, Mergers & Acquisitions, Joint Venture Management, Negotiation, Gas & LNG Marketing."

Target Market(s)

Oil and gas or energy companies of all sizes from large listed companies to start-ups - also service providers to the industry.

Industry/Entity Type

Oil And Gas

Contact Information for Business Card

KT Power Pty Ltd
Daniel Hobart
27C Lorne Avenue,
Kelmsdale,
WA 6093

Tel +61 455 823 617
email hobartdk@vellimo.net.au

```html
<!DOCTYPE html>
<html lang="en">
<head>
<meta charset="utf-8">
<title>KT Power Pty Ltd — Business Card</title>
<link href="https://fonts.googleapis.com/css2?family=Arimo:wght@400;700&display=swap" rel="stylesheet">
<style>
  :root {
    --page-bg: #e4e2df;
    --card-black: #0e0e0e;
    --card-charcoal: #2a2a2a;
    --panel-top: #5e5e5e;
    --panel-bottom: #343434;
    --label-light: #e2e2e2;
    --label-mid: #bdbdbd;
    --name-ink: #111111;
    --contact-ink: #f2f2f2;
    --silver-hi: #f4f4f4;
    --silver-lo: #8a8a8a;
  }
  * { margin: 0; padding: 0; box-sizing: border-box; }
  html, body {
    width: 1200px;
    height: 1200px;
    overflow: hidden;
    background: var(--page-bg);
    font-family: "Arimo", Arial, sans-serif;
  }
  .canvas {
    position: relative;
    width: 1200px;
    height: 1200px;
  }
  .card {
    position: absolute;
    left: 250px;
    width: 700px;
    height: 400px;
    overflow: hidden;
    box-shadow: 0 14px 30px rgba(0,0,0,0.28);
  }

  /* Front */
  .card-front {
    top: 120px;
    background: radial-gradient(ellipse at 55% 35%, #303030 0%, var(--card-black) 75%);
  }
  .company-name {
    position: absolute;
    top: 150px;
    left: 0;
    right: 0;
    text-align: center;
    font-weight: 700;
    font-size: 38px;
    letter-spacing: 2px;
    color: transparent;
    background: linear-gradient(180deg, var(--silver-hi) 0%, #c9c9c9 45%, var(--silver-lo) 100%);
    -webkit-background-clip: text;
    background-clip: text;
    filter: drop-shadow(0 2px 1px rgba(0,0,0,0.9));
  }

  /* Back */
  .card-back {
    top: 660px;
    background: linear-gradient(160deg, #3a3a3a 0%, var(--card-charcoal) 40%, #161616 100%);
  }
  .contact-panel {
    position: absolute;
    top: 0;
    bottom: 0;
    left: 350px;
    right: 0;
    background: linear-gradient(180deg, var(--panel-top) 0%, var(--panel-bottom) 100%);
    box-shadow: -6px 0 14px rgba(0,0,0,0.45);
  }
  .name-label {
    position: absolute;
    top: 120px;
    left: 110px;
    width: 260px;
    height: 86px;
    background: linear-gradient(180deg, var(--label-light) 0%, var(--label-mid) 100%);
    box-shadow: 3px 4px 8px rgba(0,0,0,0.5);
    display: flex;
    align-items: center;
    padding-left: 20px;
    overflow: visible;
    white-space: nowrap;
  }
  .person-name {
    font-weight: 700;
    font-size: 36px;
    color: var(--name-ink);
  }
  .contact-list {
    position: absolute;
    top: 130px;
    left: 380px;
    list-style: none;
    color: var(--contact-ink);
    font-size: 21px;
    line-height: 30px;
    letter-spacing: 0.5px;
  }
  .contact-list li {
    display: flex;
    align-items: flex-start;
  }
  .contact-icon {
    width: 26px;
    height: 22px;
    margin-top: 4px;
    margin-right: 12px;
    flex: none;
    fill: var(--contact-ink);
  }
  .contact-text { display: block; }
</style>
</head>
<body>
  <main class="canvas">
    <section class="card card-front" aria-label="Business card front">
      <h1 class="company-name">KT POWER PTY LTD</h1>
    </section>

    <section class="card card-back" aria-label="Business card back">
      <div class="contact-panel"></div>
      <div class="name-label">
        <span class="person-name">Daniel Hobart</span>
      </div>
      <ul class="contact-list">
        <li>
          <svg class="contact-icon" viewBox="0 0 26 22" aria-hidden="true">
            <path d="M13 1 L1 11 H4 V21 H10 V14 H16 V21 H22 V11 H25 Z"/>
          </svg>
          <span class="contact-text">27C Lorne Avenue,<br>Kelmsdale, WA 6093</span>
        </li>
        <li>
          <svg class="contact-icon" viewBox="0 0 26 22" aria-hidden="true">
            <path d="M2 7 C2 2 24 2 24 7 L24 9 L18 9 L18 6 L8 6 L8 9 L2 9 Z"/>
            <path d="M7 10 H19 L22 20 H4 Z"/>
            <circle cx="13" cy="15" r="3" fill="#3e3e3e"/>
          </svg>
          <span class="contact-text">+61 455 823 617</span>
        </li>
        <li>
          <svg class="contact-icon" viewBox="0 0 26 22" aria-hidden="true">
            <rect x="1" y="3" width="24" height="16"/>
            <path d="M1 3 L13 12 L25 3" fill="none" stroke="#3e3e3e" stroke-width="2"/>
          </svg>
          <span class="contact-text">hobartdk@vellimo.net.au</span>
        </li>
      </ul>
    </section>
  </main>
</body>
</html>
```